Business Card for a recruitment agency specializing in engineers and geeks.

I am looking to create Business Card Design for my company.
That
## Company name:
Quorvant Inc.
Quorvant is a term coined from the following concepts.
1. geek + engineer
2. geek utopia
## Company Description:
The concept of the company is to be a recruitment agency that creates a paradise for geeky engineers. We want to be a place where engineers can have more freedom and ideal career support.
# Target.
The noun itself is often given to companies that want to hire engineers, geeks, and IT-related personnel, so it would be nice to get the impression that this company seems to have good engineers and IT personnel. There are many occasions where I meet with the human resources department, president, or senior management and give it to them.
# Atmosphere
We are happy with simplicity, but with an impact that will help people remember the company. The logo is based on a dinosaur that does programming, so it should be somewhat playful, but since it will basically be used in a business setting, please don't make it too silly.
# About the logo
See the attached files. The company logo represents our engineers smiling upward because of our work, with the motif of a dinosaur doing programming.
## Color
We will leave the color scheme to you, but since the logo is in black and white, colors with such a taste would fit well.
## file format
ai, psd, png, svg
Industry/Entity Type
human resource and employment agency
Contact Information for Business Card
Company name, address, email, tel, URL,logo
Colors
Designer to choose colors to be used in the design.

```html
<!DOCTYPE html>
<html lang="en">
<head>
<meta charset="utf-8">
<title>Quorvant Inc. – Business Card</title>
<link rel="stylesheet" href="https://fonts.googleapis.com/css2?family=Exo+2:wght@600&family=Open+Sans:wght@400&display=swap">
<style>
  :root {
    --backdrop: #0fa99b;
    --card-white: #ffffff;
    --bezel: #0d0809;
    --screen-top: #1f5fa6;
    --screen-bottom: #eef2fb;
    --brand-ink: #2f3c8e;
    --window-blue: #2f78c4;
    --window-grey: #e6e6e6;
    --tag-blue: #2464b4;
    --text-dark: #1a1a1a;
  }
  * { margin: 0; padding: 0; box-sizing: border-box; }
  html, body { width: 991px; height: 1200px; overflow: hidden; }
  body { background: var(--backdrop); position: relative; font-family: "Open Sans", Arial, sans-serif; }

  .card { position: absolute; left: 136px; width: 743px; height: 480px; overflow: hidden; }
  .card--front { top: 73px; background: var(--card-white); }
  .card--back { top: 624px; background: var(--bezel); }

  /* front */
  .monitor-art {
    position: absolute; left: 99px; top: 33px; width: 544px; height: 338px;
    border-radius: 18px;
    background: linear-gradient(to bottom, var(--bezel) 0 88%, #cfcfcf 88%, #8a8a8a 100%);
  }
  .monitor-stand {
    position: absolute; left: 330px; top: 371px; width: 80px; height: 64px;
    background: linear-gradient(to right, #6e6e6e, #e8e8e8, #6e6e6e);
  }
  .monitor-base {
    position: absolute; left: 300px; top: 432px; width: 145px; height: 4px; background: #444;
  }
  .webcam {
    position: absolute; width: 14px; height: 14px; border-radius: 50%;
    background: radial-gradient(circle, #ddd 0 30%, #222 35% 55%, #fff 60%);
  }
  .monitor-art .webcam { left: 265px; top: 8px; }
  .monitor-screen {
    position: absolute; left: 29px; top: 29px; width: 487px; height: 241px;
    background: linear-gradient(to bottom, var(--screen-top), var(--screen-bottom));
  }
  .brand-name {
    position: absolute; font-family: "Exo 2", Arial, sans-serif; font-weight: 600;
    color: var(--brand-ink); white-space: nowrap;
  }
  .monitor-screen .brand-name { left: 148px; top: 168px; font-size: 40px; }
  .file-icon {
    position: absolute; left: 401px; top: 23px; width: 44px; height: 52px;
    background: #fff; border-radius: 6px;
  }
  .file-label {
    position: absolute; left: 365px; top: 90px; font-size: 8px; color: #1b2a55; white-space: nowrap;
  }

  /* back */
  .desktop {
    position: absolute; left: 0; top: 50px; width: 717px; height: 430px;
    background: linear-gradient(to bottom, var(--screen-top), var(--screen-bottom));
  }
  .card--back .webcam { left: 231px; top: 9px; width: 30px; height: 30px; }
  .desktop .brand-name { left: 62px; top: 322px; font-size: 82px; }

  .notepad {
    position: absolute; left: 236px; top: 64px; width: 461px; height: 292px;
    background: var(--window-grey); border: 1px solid #7fa9d8;
  }
  .notepad__titlebar {
    height: 40px; background: var(--window-blue); color: #fff;
    display: flex; align-items: center; padding-left: 17px; font-size: 16px; white-space: nowrap;
  }
  .notepad__titlebar > svg { margin-right: 19px; flex: none; }
  .notepad__controls { margin-left: auto; margin-right: 14px; display: flex; gap: 10px; align-items: center; }
  .notepad__menu { height: 30px; display: flex; gap: 9px; align-items: center; padding-left: 31px; font-size: 17px; color: #222; }
  .notepad__page {
    position: absolute; left: 0; top: 70px; width: 432px; height: 192px; background: #fff;
    padding: 8px 0 0 14px; font-size: 14px; line-height: 17px;
  }
  .code-line { display: flex; white-space: nowrap; }
  .code-line--field { padding-left: 12px; }
  .code-open { width: 272px; }
  .tag { color: var(--tag-blue); }
  .value { color: var(--text-dark); }
  .scroll-arrow { position: absolute; }
</style>
</head>
<body>

<section class="card card--front" aria-label="Card front">
  <div class="monitor-art" role="img" aria-label="Desktop computer monitor illustration">
    <div class="webcam"></div>
    <div class="monitor-screen">
      <div class="file-icon" aria-hidden="true"></div>
      <span class="file-label">CONTACT_INFO_quorvant.txt</span>
      <span class="brand-name">Quorvant</span>
    </div>
  </div>
  <div class="monitor-stand" aria-hidden="true"></div>
  <div class="monitor-base" aria-hidden="true"></div>
</section>

<section class="card card--back" aria-label="Card back">
  <div class="webcam"></div>
  <div class="desktop">
    <span class="brand-name">Quorvant</span>
  </div>

  <div class="notepad">
    <div class="notepad__titlebar">
      <svg width="16" height="18" viewBox="0 0 16 18" aria-hidden="true"><rect x="1" y="1" width="14" height="16" rx="2" fill="#fff"/><path d="M4 6h8M4 9h8M4 12h8" stroke="#2f78c4" stroke-width="1.2"/></svg>
      <span>--&gt;CONTACT_INFO_quorvant.txt- Notepad</span>
      <span class="notepad__controls" aria-hidden="true">
        <svg width="12" height="12"><path d="M1 10h10" stroke="#fff" stroke-width="2"/></svg>
        <svg width="14" height="12"><rect x="1" y="1" width="12" height="10" fill="none" stroke="#fff" stroke-width="2"/><path d="M1 3h12" stroke="#fff" stroke-width="3"/></svg>
        <svg width="12" height="12"><path d="M1 1l10 10M11 1L1 11" stroke="#fff" stroke-width="2"/></svg>
      </span>
    </div>
    <div class="notepad__menu"><span>File</span><span>Edit</span><span>Format</span><span>View</span></div>
    <div class="notepad__page">
      <div class="code-line"><span class="tag">&lt;card&gt;</span></div>
      <div class="code-line code-line--field"><span class="code-open"><span class="tag">&lt;name&gt;</span> <span class="value">mara lindqvist</span></span><span class="tag">&lt;/name&gt;</span></div>
      <div class="code-line code-line--field"><span class="code-open"><span class="tag">&lt;title&gt;</span> <span class="value">administrator</span></span><span class="tag">&lt;/title&gt;</span></div>
      <div class="code-line code-line--field"><span class="code-open"><span class="tag">&lt;support phone&gt;</span> <span class="value">+13579246</span></span><span class="tag">&lt;/support phone&gt;</span></div>
      <div class="code-line code-line--field"><span class="code-open"><span class="tag">&lt;direct phone&gt;</span> <span class="value">+13579246</span></span><span class="tag">&lt;/direct phone&gt;</span></div>
      <div class="code-line code-line--field"><span class="code-open"><span class="tag">&lt;email&gt;</span><span class="value">mlind@quorvant</span></span><span class="tag">&lt;/email&gt;</span></div>
      <div class="code-line code-line--field"><span class="code-open"><span class="tag">&lt;website&gt;</span> <span class="value">http://www.quorvant.com/</span></span><span class="tag">&lt;/website&gt;</span></div>
      <div class="code-line" style="margin-top:3px"><span class="tag">&lt;/card&gt;</span></div>
    </div>
    <svg class="scroll-arrow" style="left:440px;top:76px" width="12" height="8" aria-hidden="true"><path d="M1 7l5-5 5 5" fill="none" stroke="#222" stroke-width="2"/></svg>
    <svg class="scroll-arrow" style="left:440px;top:241px" width="12" height="8" aria-hidden="true"><path d="M1 1l5 5 5-5" fill="none" stroke="#222" stroke-width="2"/></svg>
    <svg class="scroll-arrow" style="left:15px;top:270px" width="8" height="12" aria-hidden="true"><path d="M7 1L2 6l5 5" fill="none" stroke="#222" stroke-width="2"/></svg>
    <svg class="scroll-arrow" style="left:414px;top:270px" width="8" height="12" aria-hidden="true"><path d="M1 1l5 5-5 5" fill="none" stroke="#222" stroke-width="2"/></svg>
  </div>
</section>

</body>
</html>
```